Carpentry company Needs a business card design

We need a design for a Carpentry / building company, business card. Please think of designs out of the ordinary and try to make it eye catching. Our existing logo will need to be incorporated in the design. However feel free to change the colours of the logo to suit your design. I would like to see some designs with green /black and orange incorporated into it.These are not the only colours accepted and all designs that appeal will be accepted.

Please contact me should you have any questions
Thanks Martin

Target Market(s)

General Public seeking carpentry work

Industry/Entity Type

Business

Contact Information for Business Card

- Current company logo ( colours can be changed)
-Phone number ,
- info@brelvanbuild.com.au
- brelvanbuild.com.au
-the facebook symbol

Font styles to use
Other font styles liked:
• You choose

Requirements
Must have
• Services we provide
• - Renovations
• -Deckings & Pergolas
• -Kitchens
• - Bathrooms
• - Intricate details
Nice to have
• an awesome design
Should not have
• Tools on the business card

```html
<!DOCTYPE html>
<html lang="en">
<head>
<meta charset="utf-8">
<title>Brelvan Build – Business Card</title>
<link href="https://fonts.googleapis.com/css2?family=Open+Sans:wght@400;600;700&display=swap" rel="stylesheet">
<style>
  :root {
    --bg: #e9e9ea;
    --ink: #231f20;
    --card-dark: #221f20;
    --white: #ffffff;
    --amber: #cf8a3f;
    --rule: #c9c9c9;
  }
  * { margin: 0; padding: 0; box-sizing: border-box; }
  html, body { width: 1151px; height: 1200px; overflow: hidden; }
  body { background: var(--bg); font-family: "Open Sans", sans-serif; position: relative; }

  .card {
    position: absolute; left: 125px; width: 900px; height: 510px;
    overflow: hidden; box-shadow: 0 6px 18px rgba(0,0,0,.18);
  }
  .card svg.bands { position: absolute; inset: 0; }

  /* back */
  .card--back { top: 50px; background: var(--card-dark); color: var(--white); }
  .brand { display: flex; align-items: center; gap: 12px; font-weight: 700; letter-spacing: 1px; white-space: nowrap; }
  .brand__mark { width: 20px; height: 20px; background: var(--amber); }
  .card--back .brand { position: absolute; right: 45px; top: 38px; font-size: 44px; color: var(--white); }
  .services { position: absolute; right: 45px; top: 120px; text-align: right; }
  .services__title { font-size: 28px; font-weight: 400; margin-bottom: 8px; }
  .services__list { list-style: none; }
  .services__list li { font-size: 20px; line-height: 28px; display: flex; justify-content: flex-end; align-items: center; gap: 10px; }
  .services__list li::after { content: ""; width: 13px; height: 13px; background: var(--amber); }
  .social { position: absolute; left: 40px; top: 447px; height: 20px; display: flex; align-items: center; gap: 10px; font-size: 16px; white-space: nowrap; }
  .social__mark { width: 18px; height: 18px; background: var(--white); }

  /* front */
  .card--front { top: 640px; background: var(--white); color: var(--ink); }
  .card--front .brand { position: absolute; left: 62px; top: 70px; font-size: 56px; color: var(--ink); }
  .name-tab { position: absolute; left: 0; top: 318px; width: 24px; height: 52px; background: var(--amber); }
  .person { position: absolute; left: 62px; top: 312px; }
  .person__name { font-size: 34px; font-weight: 600; color: var(--amber); line-height: 1.15; }
  .person__title { font-size: 21px; line-height: 1.3; }
  .divider { position: absolute; left: 62px; top: 400px; width: 640px; height: 1px; background: var(--rule); }
  .contact { position: absolute; top: 412px; display: flex; align-items: center; gap: 10px; font-size: 25px; white-space: nowrap; }
  .contact--phone { left: 62px; }
  .contact--mail { left: 365px; }
  .contact svg { fill: var(--amber); }
  .site { position: absolute; left: 54px; top: 468px; display: flex; align-items: center; gap: 8px; font-size: 22px; color: var(--white); white-space: nowrap; }
</style>
</head>
<body>

<section class="card card--back">
  <svg class="bands" width="900" height="510" viewBox="0 0 900 510" aria-hidden="true">
    <polygon points="0,442 620,442 900,288 900,318 632,472 0,472" fill="var(--amber)"/>
  </svg>
  <div class="brand"><span class="brand__mark"></span>BRELVAN BUILD</div>
  <div class="services">
    <h2 class="services__title">Services we provide</h2>
    <ul class="services__list">
      <li>Renovations</li>
      <li>Deckings &amp; Pergolas</li>
      <li>Kitchens</li>
      <li>Bathrooms</li>
      <li>Intricate details</li>
    </ul>
  </div>
  <div class="social"><span class="social__mark"></span>social.brelvanbuild.com.au</div>
</section>

<section class="card card--front">
  <svg class="bands" width="900" height="510" viewBox="0 0 900 510" aria-hidden="true">
    <polygon points="0,458 790,458 900,358 900,398 800,510 0,510" fill="var(--amber)"/>
    <rect x="876" y="430" width="24" height="62" fill="var(--amber)"/>
  </svg>
  <div class="brand"><span class="brand__mark"></span>BRELVAN BUILD</div>
  <div class="name-tab"></div>
  <div class="person">
    <p class="person__name">Your Name</p>
    <p class="person__title">Job Title</p>
  </div>
  <div class="divider"></div>
  <div class="contact contact--phone">
    <svg width="16" height="24" viewBox="0 0 16 24" aria-hidden="true"><path d="M2 2h12v20H2z M4 4v6h8V4z M4 13h2v2H4z M7 13h2v2H7z M10 13h2v2h-2z M4 16h2v2H4z M7 16h2v2H7z M10 16h2v2h-2z" fill-rule="evenodd"/></svg>
    <span>000-111-222-33</span>
  </div>
  <div class="contact contact--mail">
    <svg width="28" height="18" viewBox="0 0 28 18" aria-hidden="true"><path d="M0 0h28v18H0z M2 2l12 9 12-9v1L14 12 2 3z M2 16l8-7 1 1-8 6z M26 16l-8-7-1 1 8 6z" fill-rule="evenodd"/></svg>
    <span>info@brelvanbuild.com.au</span>
  </div>
  <div class="site">
    <svg width="22" height="22" viewBox="0 0 22 22" aria-hidden="true"><circle cx="11" cy="11" r="9" fill="none" stroke="#fff" stroke-width="2"/><path d="M6 6c3 1 3 4 1 6s1 4 2 6M14 4c-1 3 2 3 4 4M13 12c2 0 3 2 2 5" fill="none" stroke="#fff" stroke-width="1.6"/></svg>
    <span>brelvanbuild.com.au</span>
  </div>
</section>

</body>
</html>
```